Dental Hygiene referral cards

I am looking to make some referral cards for our hygienists for our dental office. something with our logo and address on the front, and on the back have
hygienist:
__________________
Referred by:
__________________
with a little blurb about what we will give away for a referral.

attached to this is our logo, and a drawing of what im looking for.

I will need this for two of our offices, so just the logo and address will change.

```html
<!DOCTYPE html>
<html lang="en">
<head>
<meta charset="UTF-8">
<title>Riverbend Dental – Referral Card</title>
<link rel="stylesheet" href="https://fonts.googleapis.com/css2?family=Work+Sans:wght@400;500;600&display=swap">
<style>
  :root {
    --bg: #262626;
    --card: #ffffff;
    --brand-blue: #1d4a8a;
    --band-top: #173f7a;
    --band-bottom: #245493;
    --ink-grey: #8a8a8a;
    --rule-grey: #bdbdbd;
    --white: #ffffff;
  }
  * { box-sizing: border-box; margin: 0; padding: 0; }
  html, body {
    width: 1200px; height: 900px; overflow: hidden;
    background: var(--bg);
    font-family: "Work Sans", Arial, sans-serif;
  }
  .canvas {
    position: relative; width: 1200px; height: 900px;
  }
  .card {
    position: absolute; left: 260px;
    width: 680px; height: 389px;
    background: var(--card);
    overflow: hidden;
  }
  .card--back { top: 50px; }
  .card--front { top: 461px; }

  /* Back side */
  .offer-band {
    position: absolute; left: 0; top: 0; width: 100%; height: 185px;
    background: linear-gradient(90deg, var(--band-top), var(--band-bottom));
    color: var(--white);
    text-transform: uppercase;
    letter-spacing: 0.14em;
    font-size: 15px; line-height: 1.55;
  }
  .offer-title {
    position: absolute; left: 44px; top: 30px;
  }
  .offer-title .lead { text-transform: none; }
  .offer-blurb {
    position: absolute; right: 40px; top: 78px;
    text-align: right; font-size: 14.5px;
  }
  .referral-fields {
    position: absolute; left: 44px; right: 44px; top: 208px;
  }
  .field {
    color: var(--brand-blue);
    font-size: 18px; letter-spacing: 0.06em;
    padding-bottom: 10px;
    border-bottom: 1px solid var(--rule-grey);
    margin-bottom: 44px;
  }

  /* Front side */
  .brand {
    position: absolute; left: 40px; top: 184px;
    width: 290px;
    display: flex; align-items: center; gap: 10px;
    color: var(--brand-blue);
    font-weight: 600; font-size: 22px; letter-spacing: 0.03em;
    line-height: 1; white-space: nowrap;
    text-transform: uppercase;
  }
  .brand-dot {
    width: 16px; height: 16px; border-radius: 50%;
    background: var(--brand-blue); flex: none;
  }
  .divider {
    position: absolute; left: 356px; top: 108px;
    width: 3px; height: 180px; background: var(--brand-blue);
  }
  .contact {
    position: absolute; left: 392px; top: 108px;
    color: var(--ink-grey); font-size: 17px; line-height: 1.4;
  }
  .contact-name {
    color: var(--brand-blue); font-weight: 600;
    font-size: 26px; letter-spacing: 0.02em; line-height: 1.1;
  }
  .contact-role { font-size: 17px; margin-bottom: 12px; }
  .contact-address { margin-bottom: 8px; }
  .contact-line { display: flex; align-items: center; gap: 10px; }
  .contact-line svg { width: 13px; height: 13px; flex: none; }
</style>
</head>
<body>
<main class="canvas">

  <section class="card card--back" aria-label="Referral card, back">
    <div class="offer-band">
      <p class="offer-title"><span class="lead">Free</span><br>SonaBright<br>Toothbrush!</p>
      <p class="offer-blurb">Refer a paitent for an<br>exam and a cleaning and both<br>of you will reeleve a free<br>SonaBright tooth brush!</p>
    </div>
    <div class="referral-fields">
      <p class="field">Hygienist:</p>
      <p class="field">Referred by:</p>
    </div>
  </section>

  <section class="card card--front" aria-label="Referral card, front">
    <div class="brand"><span class="brand-dot"></span>Riverbend Dental</div>
    <div class="divider"></div>
    <div class="contact">
      <p class="contact-name">DANIEL HARPER</p>
      <p class="contact-role">Director</p>
      <p class="contact-address">4820 Maple Crest Lane<br>Fairview, KY 41090</p>
      <p class="contact-line">
        <svg viewBox="0 0 16 16" aria-hidden="true"><path d="M4 1 L6.5 4 L5 6 Q7 10 10 11 L12 9.5 L15 12 L13 15 Q5 14 1 4 Z" fill="none" stroke="#1d4a8a" stroke-width="1.6" stroke-linejoin="round"/></svg>
        0400 555 012
      </p>
      <p class="contact-line">
        <svg viewBox="0 0 16 16" aria-hidden="true"><rect x="1.5" y="3.5" width="13" height="9" fill="none" stroke="#1d4a8a" stroke-width="1.6"/><path d="M1.5 3.5 L8 9 L14.5 3.5" fill="none" stroke="#1d4a8a" stroke-width="1.6"/></svg>
        info@riverbenddental.com
      </p>
      <p class="contact-line">
        <svg viewBox="0 0 16 16" aria-hidden="true"><circle cx="8" cy="8" r="6.5" fill="none" stroke="#1d4a8a" stroke-width="1.4"/><ellipse cx="8" cy="8" rx="3" ry="6.5" fill="none" stroke="#1d4a8a" stroke-width="1.2"/><path d="M1.5 8 H14.5" stroke="#1d4a8a" stroke-width="1.2"/></svg>
        www.riverbenddental.com
      </p>
    </div>
  </section>

</main>
</body>
</html>
```